Rack Card for Willow Bend Dog Training

I love the logo you designed for me a while back (I had it updated and have the new files).

I need a rack card designed, 2 sided.

One side will be Willow Bend Dog Training (my general dog training business)

The other side will be my Deaf and Blind Dog Training Business speciality.

Both sides Full Color/4 color

3.5 x 8.5 inches

I can provide photos and text accordingly.

Let me know the estimated price and Turn around time.

```html
<!DOCTYPE html>
<html lang="en">
<head>
<meta charset="utf-8">
<title>Willow Bend Dog Training – Rack Card</title>
<link href="https://fonts.googleapis.com/css2?family=Source+Sans+3:wght@400;600;700&display=swap" rel="stylesheet">
<style>
  :root {
    --orange: #ff6a00;
    --orange-deep: #f25c00;
    --ink: #1f1f1f;
    --white: #ffffff;
    --backdrop: #a4a4a4;
    --rule-red: #d8342a;
  }
  * { margin: 0; padding: 0; box-sizing: border-box; }
  html, body { width: 1200px; height: 904px; overflow: hidden; }
  body {
    background: var(--backdrop);
    font-family: "Source Sans 3", "Segoe UI", sans-serif;
    color: var(--ink);
    position: relative;
  }
  .rack-card {
    position: absolute;
    top: 133px;
    width: 291px;
    height: 708px;
    overflow: hidden;
  }
  .rack-card--front { left: 354px; background: var(--white); }
  .rack-card--back { left: 704px; background: var(--orange); color: var(--white); }
  .card-shapes { position: absolute; inset: 0; width: 291px; height: 708px; }
  .abs { position: absolute; }
  .photo { position: absolute; }
  .photo--round { border-radius: 50%; border: 2px solid var(--white); }

  .brand-name {
    position: absolute;
    font-weight: 700;
    font-size: 19px;
    line-height: 20px;
    display: flex;
    align-items: center;
    gap: 6px;
    white-space: nowrap;
  }
  .brand-name .brand-dot { width: 10px; height: 10px; border-radius: 50%; flex: none; }
  .rack-card--front .brand-name { color: var(--ink); }
  .rack-card--front .brand-dot { background: var(--orange); }
  .rack-card--back .brand-name { color: var(--white); font-size: 17px; }
  .rack-card--back .brand-dot { border: 1.5px solid var(--white); }

  .services-title {
    left: 118px; top: 143px; width: 174px;
    text-align: center;
    color: var(--orange);
    font-weight: 700;
    font-size: 20px;
    line-height: 22px;
  }
  .services-list {
    left: 118px; top: 212px; width: 174px;
    list-style: none;
    text-align: center;
    font-size: 10.5px;
    line-height: 15px;
    font-weight: 600;
  }
  .intro-headline {
    left: 20px; top: 384px;
    color: var(--white);
    font-weight: 700;
    font-size: 12px;
    line-height: 13.8px;
    white-space: nowrap;
  }
  .intro-body {
    left: 20px; top: 431px;
    color: var(--white);
    font-size: 9.3px;
    line-height: 11.8px;
    white-space: nowrap;
  }
  .cta-title {
    color: var(--orange);
    font-weight: 700;
    font-size: 11.5px;
    line-height: 14px;
    letter-spacing: 0.2px;
    text-transform: uppercase;
    white-space: nowrap;
  }
  .contact-row {
    position: absolute;
    display: flex;
    align-items: center;
    gap: 4px;
    white-space: nowrap;
    color: var(--ink);
  }
  .contact-row--phone { font-size: 10.5px; font-weight: 600; }
  .contact-row--phone .region { font-weight: 700; }
  .contact-row--small { font-size: 9.3px; }
  .contact-icon { width: 9px; height: 9px; flex: none; }

  .back-title {
    left: 0; top: 17px; width: 291px;
    text-align: center;
    font-weight: 700;
    font-size: 19px;
    line-height: 22px;
  }
  .section-heading {
    font-weight: 700;
    font-size: 11.5px;
    line-height: 13px;
    white-space: nowrap;
  }
  .section-text {
    font-size: 8.5px;
    line-height: 10.5px;
    white-space: nowrap;
  }
  .section-text p + p { margin-top: 4.3px; }
</style>
</head>
<body>

<!-- Front: general training -->
<section class="rack-card rack-card--front" aria-label="Willow Bend Dog Training rack card, front">
  <svg class="card-shapes" viewBox="0 0 291 708" aria-hidden="true">
    <circle cx="-8" cy="22" r="72" fill="none" stroke="var(--orange)" stroke-width="0.8"/>
    <circle cx="302" cy="92" r="58" fill="none" stroke="var(--orange)" stroke-width="0.8"/>
    <path d="M0 355 C50 372 110 368 150 345 C185 325 210 310 240 315 C265 320 280 328 291 336 L291 708 L0 708 Z" fill="var(--orange)"/>
    <path d="M0 608 C40 588 100 576 150 579 C200 582 240 593 291 618" fill="none" stroke="var(--white)" stroke-width="1"/>
    <path d="M0 615 C40 595 100 583 150 586 C200 589 240 600 291 625 L291 708 L0 708 Z" fill="var(--white)"/>
  </svg>

  <div class="brand-name" style="left:92px; top:62px;"><span class="brand-dot"></span>Willow Bend</div>

  <div class="photo" role="img" aria-label="Photo of a black and white shepherd dog sitting with one paw raised"
       style="left:0; top:136px; width:142px; height:225px; background:linear-gradient(160deg,#f2f2f2 0%,#6b6b6b 35%,#2a2a2a 70%,#d9d2c8 100%); border-radius:40% 40% 10% 10%;"></div>

  <h1 class="abs services-title">Dog Training<br>&amp; Behavioral<br>Services</h1>
  <ul class="abs services-list">
    <li>• Puppy Training</li>
    <li>• House Breaking</li>
    <li>• Leash Training • Obedience</li>
    <li>• Rescue Dog Training</li>
    <li>• Separation Anxiety</li>
    <li>• Socialization</li>
  </ul>

  <div class="photo photo--round" role="img" aria-label="Photo of the trainer sitting with her shepherd mix dog"
       style="left:176px; top:358px; width:118px; height:118px; background:linear-gradient(150deg,#c9d8c2 0%,#8a6b4e 40%,#3d4a5e 75%,#b9915f 100%);"></div>

  <h2 class="abs intro-headline">Having a happy,<br>well-balanced dog is one<br>of life’s greatest pleasures!</h2>
  <p class="abs intro-body">At Willow Bend, we believe that<br>the goal of every dog owner is<br>to have a loving, well-behaved<br>companion. However, some dogs<br>develop unwanted behaviors that are<br>frustrating or create unsafe situations. Our<br>expert Los Angeles dog trainer educates pet owners &amp;<br>trains dogs to be happy, safe companions. Whatever the<br>age or breed of your dog, Willow Bend can help you and<br>your pet achieve harmonious, well-balanced behavior to<br>create a loving home &amp; happy environment for you both.</p>

  <div class="photo" role="img" aria-label="Photo of a tan and white basenji raising a paw"
       style="left:190px; top:570px; width:101px; height:138px; background:linear-gradient(170deg,#c4743a 0%,#a65a28 45%,#f1e6da 100%); border-radius:45% 45% 0 0;"></div>

  <p class="abs cta-title" style="left:20px; top:619px;">Schedule free 15 minute<br>phone consultation</p>
  <div class="contact-row contact-row--phone" style="left:20px; top:648px;">
    <span class="region">Orange county</span>
    <svg class="contact-icon" viewBox="0 0 10 10"><circle cx="5" cy="5" r="4.4" fill="none" stroke="var(--orange)" stroke-width="0.9"/><path d="M3.4 2.8 L4.2 2.6 L4.6 3.8 L4 4.3 Q4.6 5.6 5.7 6 L6.2 5.4 L7.4 5.8 L7.2 6.6 Q5.8 7.4 4.3 5.9 Q2.8 4.4 3.4 2.8 Z" fill="var(--orange)"/></svg>
    <span>(714) 555-0142</span>
  </div>
  <div class="contact-row contact-row--phone" style="left:20px; top:665px;">
    <span class="region">Los angeles</span>
    <svg class="contact-icon" viewBox="0 0 10 10"><circle cx="5" cy="5" r="4.4" fill="none" stroke="var(--orange)" stroke-width="0.9"/><path d="M3.4 2.8 L4.2 2.6 L4.6 3.8 L4 4.3 Q4.6 5.6 5.7 6 L6.2 5.4 L7.4 5.8 L7.2 6.6 Q5.8 7.4 4.3 5.9 Q2.8 4.4 3.4 2.8 Z" fill="var(--orange)"/></svg>
    <span>(310) 555-0187</span>
  </div>
  <div class="contact-row contact-row--small" style="left:20px; top:681px;">
    <svg class="contact-icon" viewBox="0 0 10 10"><circle cx="5" cy="5" r="4.3" fill="none" stroke="var(--orange)" stroke-width="0.9"/><ellipse cx="5" cy="5" rx="1.9" ry="4.3" fill="none" stroke="var(--orange)" stroke-width="0.7"/><path d="M0.8 5 H9.2" stroke="var(--orange)" stroke-width="0.7"/></svg>
    <span>www.willowbenddogtraining.com</span>
  </div>
</section>

<!-- Back: deaf & blind speciality -->
<section class="rack-card rack-card--back" aria-label="Willow Bend Dog Training rack card, back">
  <svg class="card-shapes" viewBox="0 0 291 708" aria-hidden="true">
    <circle cx="42" cy="-42" r="57" fill="none" stroke="var(--white)" stroke-width="0.8"/>
    <path d="M0 568 C40 538 100 521 160 523 C220 525 260 548 291 573" fill="none" stroke="var(--white)" stroke-width="1"/>
    <path d="M0 575 C40 545 100 528 160 530 C220 532 260 555 291 580 L291 708 L0 708 Z" fill="var(--white)"/>
    <path d="M0 648 H190" stroke="var(--rule-red)" stroke-width="0.6"/>
  </svg>

  <h1 class="abs back-title">Deaf &amp; Blind Dog Training</h1>

  <h2 class="abs section-heading" style="left:19px; top:53px;">Deaf Dog Training</h2>
  <div class="abs section-text" style="left:21px; top:67px;">
    <p>Deaf dogs can easily be trained using<br>hand signals.</p>
    <p>We owe it to our dogs to teach them<br>how to behave, and that the world is a<br>safe place.</p>
    <p>A dog with special needs is no exception.</p>
    <p>Training a dog that is deaf can come with<br>it challenges.</p>
  </div>
  <div class="photo photo--round" role="img" aria-label="Photo of a happy brown and white border collie on a beach"
       style="left:183px; top:55px; width:114px; height:114px; background:linear-gradient(160deg,#9fb4c4 0%,#7a4a2c 45%,#f4f1ec 80%,#d8cdbb 100%);"></div>

  <div class="photo photo--round" role="img" aria-label="Photo of an older golden retriever being petted on the head"
       style="left:-2px; top:201px; width:100px; height:100px; background:linear-gradient(160deg,#8a5a32 0%,#c98d4f 45%,#a36a3b 80%,#6a4327 100%);"></div>
  <h2 class="abs section-heading" style="left:108px; top:192px;">Blind Dog Training</h2>
  <div class="abs section-text" style="left:112px; top:206px;">
    <p>Deaf dogs can easily be trained using<br>&nbsp;sound signals.</p>
    <p>&nbsp;&nbsp;We owe it to our dogs to teach them how<br>&nbsp;&nbsp;to behave, to know their surrounding<br>&nbsp;&nbsp;even with their sight is loss, and that<br>&nbsp;the world is a safe place.</p>
    <p>A dog with special needs is no exception.</p>
  </div>
  <div class="abs section-text" style="left:91px; top:293px; text-align:center;">
    <p>Owners can wear a jingling bell, so your<br>blind dog can find you.</p>
  </div>
  <div class="abs section-text" style="left:21px; top:318px;">
    <p>Blind Dogs have EXTREMELY heightened senses (especially smell<br>and sound).</p>
  </div>

  <h2 class="abs section-heading" style="left:20px; top:368px;">Deaf / Blind Dog Training</h2>
  <div class="abs section-text" style="left:21px; top:382px;">
    <p>Deaf/Blind dogs can easily be trained<br>using touch and tactile cues.</p>
    <p>We owe it to our dogs to teach them how<br>to behave, to know their surroundings<br>even when their sight &amp; hearing is lost,<br>&amp; that the world is a safe place.</p>
    <p>A dog with special needs is no exception.</p>
    <p>Training a dog that is both blind &amp; deaf can<br>come with its own challenges, we have many<br>years of experience to help.</p>
  </div>
  <div class="photo photo--round" role="img" aria-label="Photo of a white dog wearing a service vest in a garden"
       style="left:184px; top:362px; width:114px; height:114px; background:linear-gradient(150deg,#5d7a3a 0%,#8aa55a 35%,#eeeeee 65%,#7d6a55 100%);"></div>

  <div class="brand-name" style="left:168px; top:497px;"><span class="brand-dot"></span>Willow Bend</div>

  <div class="photo" role="img" aria-label="Photo of a terrier holding a tin can telephone to its ear"
       style="left:190px; top:575px; width:101px; height:133px; background:linear-gradient(170deg,#b06a34 0%,#c9c9c9 40%,#f3f1ee 70%,#e8e4de 100%); border-radius:45% 45% 0 0;"></div>

  <p class="abs cta-title" style="left:20px; top:565px;">Schedule free 15 minute<br>phone consultation</p>
  <div class="contact-row contact-row--phone" style="left:20px; top:595px;">
    <span class="region">Orange county</span>
    <svg class="contact-icon" viewBox="0 0 10 10"><circle cx="5" cy="5" r="4.4" fill="none" stroke="var(--orange)" stroke-width="0.9"/><path d="M3.4 2.8 L4.2 2.6 L4.6 3.8 L4 4.3 Q4.6 5.6 5.7 6 L6.2 5.4 L7.4 5.8 L7.2 6.6 Q5.8 7.4 4.3 5.9 Q2.8 4.4 3.4 2.8 Z" fill="var(--orange)"/></svg>
    <span>(714) 555-0142</span>
  </div>
  <div class="contact-row contact-row--phone" style="left:20px; top:611px;">
    <span class="region">Los angeles</span>
    <svg class="contact-icon" viewBox="0 0 10 10"><circle cx="5" cy="5" r="4.4" fill="none" stroke="var(--orange)" stroke-width="0.9"/><path d="M3.4 2.8 L4.2 2.6 L4.6 3.8 L4 4.3 Q4.6 5.6 5.7 6 L6.2 5.4 L7.4 5.8 L7.2 6.6 Q5.8 7.4 4.3 5.9 Q2.8 4.4 3.4 2.8 Z" fill="var(--orange)"/></svg>
    <span>(310) 555-0187</span>
  </div>
  <div class="contact-row contact-row--small" style="left:20px; top:629px;">
    <svg class="contact-icon" viewBox="0 0 10 10"><circle cx="5" cy="5" r="4.3" fill="none" stroke="var(--orange)" stroke-width="0.9"/><rect x="2.6" y="3.3" width="4.8" height="3.4" fill="none" stroke="var(--orange)" stroke-width="0.7"/><path d="M2.6 3.3 L5 5.2 L7.4 3.3" fill="none" stroke="var(--orange)" stroke-width="0.7"/></svg>
    <span>hello@willowbenddogs.com</span>
  </div>
  <div class="contact-row contact-row--small" style="left:20px; top:653px;">
    <svg class="contact-icon" viewBox="0 0 10 10"><circle cx="5" cy="5" r="4.3" fill="none" stroke="var(--orange)" stroke-width="0.9"/><ellipse cx="5" cy="5" rx="1.9" ry="4.3" fill="none" stroke="var(--orange)" stroke-width="0.7"/><path d="M0.8 5 H9.2" stroke="var(--orange)" stroke-width="0.7"/></svg>
    <span>www.willowbenddogtraining.com</span>
  </div>
  <div class="contact-row contact-row--small" style="left:20px; top:669px; align-items:flex-start;">
    <svg class="contact-icon" viewBox="0 0 10 10" style="margin-top:1px;"><circle cx="5" cy="5" r="4.3" fill="none" stroke="var(--orange)" stroke-width="0.9"/><path d="M5 7.6 C3.6 6 3.1 5.1 3.1 4.3 A1.9 1.9 0 0 1 6.9 4.3 C6.9 5.1 6.4 6 5 7.6 Z" fill="none" stroke="var(--orange)" stroke-width="0.7"/></svg>
    <span>4810 Maple Crest Ave.<br>Suite B-118 Brea CA 92821</span>
  </div>
</section>

</body>
</html>
```